Need a Middle Eastern/Cooking/Nutrition Design please :)

Hi I am looking to revamp my Middle Eastern/Cooking/Nutrition Blog for something that is clean, sophisticated yet sultry. My site now www.flavorsofthedunes.com is messy and needs more color help with background. Please send anything you think is suitable for the concept.
Target Market(s)
high end
Industry/Entity Type
Nutrition
Requirements
Must have
- Your work looks wonderful!
I am looking forward to your designs! I am really trying to revamp my current site www.flavorsofthedunes.com to be more clean and sophisticated.
I like this color palette or maybe royal purple and gold. http://www.huegatherers.net/palette/412907/The_Desert_Dusk
I had my website evaluated by a brand specialist and this what she said I should be doing :) Let me know what you think- really appreciate it!
Comments Below:
Given your brand identity, I think you want to go for something clean and simple but with touches of bold color and iconography. You want the site to come off as approachable, but to also have an exotic and slightly mysterious edge. Perhaps choose a solid background color and use stylish icons, flourishes and images to bring the Middle Eastern/Mediterranean flavor.
I also recommend that you use a neutral color or a whitewashed design as your background. It is easier on the eyes to read a lot of text when it’s a neutral (light or white) background color with a darker font.
Here is a color palette that I like for you: http://www.huegatherers.net/palette/412907/The_Desert_Dusk
In terms of organization, I think it would be great to have your home page be a jump page. So, rather than having a list of your recent posts, perhaps you can welcome guests with a picture of yourself/your food/your brand.
Then, you could have a menu of options for people to explore your site (kind of like the bar you have at the top of your page now). But instead of just having the text, you could use images as the links to the different pages. This would include a link to classes, recipes, nutritional information, products, TV shows/videos, bio, etc. And you could organize it in a creative way on the page.
There are so many ways that you can organize your site, and it’s completely up to you! But here are some examples that I think you could look to for inspiration:
http://lorenabrevicelli.com/
http://www.sunlitmarquise.com/
http://www.dybelin.com/
http://www.trylentilo.com/trylentilo.com/Lentilo.html
http://www.korubrisk.com/
http://www.velukebab.com/
For your brand name, ultimately, you want something that reflects the down to earth yet somewhat exotic nature of your brand. The actual brand name is up to you…but I do like where you’re going with the ingredients.
I want simple and sophisticated yet also portrays the mysterious and exotic Middle East. The site colors and pictures should transport people but also want it clean. I think my site is too busy now.
The content and layout could be the same but the logo, domain name possible and website name, background and color scheme all have to change although I do like dark purple and gold as possibilities along with the color pattern I sent already,
Im not sure if its a single page or full project but I do want a total revamp of the scheme- do you need to redo the website or just remake the existing because I can provide the website info if thats the case . I can pay the up front cost now. I believe the quote is 300.
Also im not sure if I should stick with the Sumac up name or here are other name options if you think they meet the sophisticated brand of the Middle East more.
tahini & honey
fig & chickpea
saffron & rosewater- very exotic
harissa & honey
pomegranates & pistachios
saffron & pomegranates
figs & saffron
The name should be playful and fun for the site. I like the idea of ingredients because it brings both the Mediterranean and Middle East imagery and allows for broad appeal.
Thank you soooooooooo much- I know it’s a lot to think about and I greatly appreciate your insight and talents in this!!
Nice to have
- Clean, sophisticated, sultry, exotic and professional
Should not have
- too busy

```html
<!DOCTYPE html>
<html lang="en">
<head>
<meta charset="utf-8">
<title>Sumac up – Taste of the Mediterranean &amp; Middle East</title>
<link href="https://fonts.googleapis.com/css2?family=Arimo:wght@400;700&family=Lora:ital@1&display=swap" rel="stylesheet">
<style>
:root{
  --header-dark:#2f2826;
  --band-top:#8a6a62;
  --band-bottom:#5a403b;
  --plum:#4c2a3a;
  --plum-label:#5e3445;
  --coral:#f06f78;
  --coral-light:#f58a90;
  --coral-title:#f0707a;
  --paper:#ffffff;
  --mist:#efeeee;
  --ink:#3c3a3a;
  --ink-soft:#555;
  --cream:#efe6d6;
  --tile:#e8dcc6;
}
*{box-sizing:border-box;margin:0;padding:0}
html,body{width:1067px;height:1200px;overflow:hidden}
body{position:relative;background:var(--mist);font-family:"Arimo",Arial,sans-serif;color:var(--ink)}
.abs{position:absolute}

.site-header{left:0;top:0;width:1067px;height:153px;background:var(--header-dark)}
.nav-band{left:0;top:117px;width:1067px;height:35px;background:linear-gradient(var(--band-top),var(--band-bottom));border-bottom:1px solid #c9b5ad}
.brand{left:84px;top:52px;display:flex;align-items:center;gap:10px}
.brand-dot{width:20px;height:20px;border-radius:50%;background:#8fa33a}
.brand-name{font-size:38px;font-weight:700;color:var(--cream);letter-spacing:1px;line-height:44px}
.brand-tag{left:80px;top:124px;width:208px;text-align:center;white-space:nowrap;font-size:8px;font-weight:700;color:var(--cream);letter-spacing:.3px}

.subscribe-label{left:720px;top:64px;font-size:13px;color:#b9aea6}
.email-field{left:723px;top:86px;width:157px;height:21px;border:1px solid #8c8480;border-radius:5px;background:#3a3432;color:#e8e2de;font-size:11px;line-height:19px;padding-left:8px}
.go-btn{left:888px;top:86px;width:39px;height:21px;border:1px solid #8c8480;border-radius:4px;background:#3a3432;color:#e8e2de;font-size:11px;line-height:19px;text-align:center}
.social-small{top:77px;width:25px;height:31px;background:var(--tile);border:1px solid #b8a890}

.main-nav{right:20px;top:117px;height:35px;display:flex;align-items:center}
.main-nav a{color:#fff;text-decoration:none;font-size:13.5px;padding:0 14px;border-left:1px solid #c4aaa2;line-height:22px}
.main-nav a:first-child{border-left:0}

.hero{left:0;top:153px;width:1067px;height:436px;background:var(--plum)}
.hero-frame{left:28px;top:162px;width:1009px;height:416px;background:var(--paper)}
.hero-photo{left:39px;top:168px;width:986px;height:403px;background:
  radial-gradient(circle at 27% 55%,#7a4526 0,#6a3a20 14%,rgba(106,58,32,0) 26%),
  radial-gradient(ellipse 22% 14% at 27% 23%,#e6e1da 0,rgba(230,225,218,0) 100%),
  radial-gradient(ellipse 16% 20% at 48% 22%,#6b4a33 0,rgba(107,74,51,0) 100%),
  radial-gradient(ellipse 16% 17% at 70% 24%,#d9482e 0,rgba(217,72,46,0) 100%),
  radial-gradient(ellipse 26% 26% at 57% 62%,#d9ccb0 0,#c9b894 50%,rgba(201,184,148,0) 100%),
  radial-gradient(ellipse 30% 40% at 88% 70%,#3f6a24 0,rgba(63,106,36,0) 100%),
  radial-gradient(ellipse 25% 30% at 12% 85%,#35521f 0,rgba(53,82,31,0) 100%),
  linear-gradient(90deg,#4a3526,#6e5a44 40%,#c8c2bb 80%,#2c2622)}
.hero-arrow{top:362px;width:45px;height:80px;background:rgba(20,20,20,.75);border-radius:8px}
.hero-arrow svg{position:absolute;left:14px;top:28px}
.hero-quote{left:39px;top:499px;width:986px;height:72px;background:rgba(30,30,30,.72);font-family:"Lora",Georgia,serif;font-style:italic;font-size:17px;line-height:26px;color:#e8e4de;padding:11px 60px 0 25px}

.tiles-top{left:0;top:589px;width:1067px;height:234px;background:var(--paper)}
.tile-photo{height:183px;border:3px solid var(--coral);border-radius:5px}
.tile-photo.plum{border-color:var(--plum-label)}
.tile-label{height:34px;border-radius:3px;background:linear-gradient(var(--coral-light),var(--coral));color:#fff;font-size:14.5px;line-height:34px;padding:0 10px;display:flex;justify-content:space-between}
.tile-label.plum{background:var(--plum-label)}

.news-title{left:69px;top:830px;font-size:17px;font-weight:700;color:var(--coral-title)}
.news-item{left:70px;width:285px;font-size:14px;line-height:22px;color:var(--ink-soft)}
.news-item h3{font-size:17px;color:var(--ink);font-weight:700;line-height:26px}
.news-rule{left:70px;top:942px;width:284px;height:1px;background:#8a8686}
.view-all{left:277px;top:1036px;font-size:13.5px;color:var(--coral);border-bottom:1px solid var(--coral);line-height:17px}

.site-footer{left:0;top:1065px;width:1067px;height:135px;background:var(--header-dark)}
.footer-nav{left:70px;top:1077px;font-size:13px;color:#fff;word-spacing:1px}
.footer-nav span{margin:0 6px}
.copyright{left:69px;top:1101px;font-size:13px;color:#fff}
.social-large{top:1084px;width:44px;height:55px;background:var(--tile);border:1px solid #b8a890;font-size:10px;color:#6b5e4e;text-align:center;padding-top:36px}
</style>
</head>
<body>
<header class="abs site-header"></header>
<div class="abs nav-band"></div>
<div class="abs brand"><span class="brand-dot"></span><span class="brand-name">Sumac up</span></div>
<div class="abs brand-tag">TASTE OF THE MEDITERRANEAN &amp; MIDDLE EAST</div>

<div class="abs subscribe-label">Subscribe to our mailing list</div>
<div class="abs email-field">email address ...</div>
<div class="abs go-btn">GO</div>
<div class="abs social-small" style="left:942px"></div>
<div class="abs social-small" style="left:969px"></div>
<div class="abs social-small" style="left:996px"></div>

<nav class="abs main-nav">
  <a>Home</a><a>Why Mediterranean &amp; MidEast Cuisine?</a><a>Cooking Class</a><a>Healthy Recipes</a><a>About</a><a>Contact</a>
</nav>

<section class="abs hero"></section>
<div class="abs hero-frame"></div>
<div class="abs hero-photo" role="img" aria-label="Plate of falafel with tahini, hummus topped with pomegranate seeds, tomato and parsley"></div>
<div class="abs hero-arrow" style="left:39px"><svg width="16" height="24" viewBox="0 0 16 24"><path d="M3 3l9 9-9 9" fill="none" stroke="#ddd" stroke-width="3"/></svg></div>
<div class="abs hero-arrow" style="left:980px"><svg width="16" height="24" viewBox="0 0 16 24"><path d="M13 3L4 12l9 9" fill="none" stroke="#ddd" stroke-width="3"/></svg></div>
<div class="abs hero-quote">We are indeed much more than what we eat, but what we eat can nevertheless help us to be much more than what we are. ~Marguerite Haldane</div>

<section class="abs tiles-top"></section>
<div class="abs tile-photo" style="left:65px;top:598px;width:297px;background:radial-gradient(ellipse 40% 35% at 25% 40%,#d8b888 0,rgba(216,184,136,0) 100%),radial-gradient(ellipse 45% 40% at 70% 30%,#3a3a5a 0,rgba(58,58,90,0) 100%),radial-gradient(ellipse 50% 40% at 55% 85%,#c9622a 0,rgba(201,98,42,0) 100%),linear-gradient(160deg,#8a4a22,#6a2a1a 55%,#b8753a)" role="img" aria-label="Middle Eastern table spread with bread, skewers and tea glasses"></div>
<div class="abs tile-label" style="left:65px;top:787px;width:297px"><span>Register For A Cooking Class</span><span>&gt;&gt;</span></div>
<div class="abs tile-photo plum" style="left:376px;top:598px;width:296px;background:radial-gradient(ellipse 28% 45% at 48% 45%,#6a4a3a 0,rgba(106,74,58,0) 100%),radial-gradient(ellipse 30% 35% at 18% 65%,#2a4ab0 0,rgba(42,74,176,0) 100%),radial-gradient(ellipse 35% 45% at 85% 55%,#eceaf2 0,rgba(236,234,242,0) 100%),linear-gradient(180deg,#8e8cc0,#6a6ab0 50%,#3a4aa0)" role="img" aria-label="Portrait of the cook in front of a blue-domed seaside town"></div>
<div class="abs tile-label plum" style="left:376px;top:787px;width:296px"><span>Meet Nadia The Cook</span><span>&gt;&gt;</span></div>
<div class="abs tile-photo" style="left:685px;top:598px;width:297px;background:radial-gradient(ellipse 35% 30% at 62% 60%,#d8c850 0,rgba(216,200,80,0) 100%),radial-gradient(ellipse 35% 60% at 10% 45%,#4a5a2a 0,rgba(74,90,42,0) 100%),linear-gradient(135deg,#8a8a4a,#c9c08a 45%,#e4e8ec)" role="img" aria-label="Bowl of olive oil with olive branches"></div>
<div class="abs tile-label" style="left:685px;top:787px;width:297px"><span>Benefits of Middle Eastern</span><span>&gt;&gt;</span></div>

<div class="abs news-title">News &gt; Spring Dates!</div>
<div class="abs news-item" style="top:864px"><h3>February 19</h3>6:30pm-9:30pm at Hearth Lab NYC: 412 West 48th Street, New York, NY</div>
<div class="abs news-rule"></div>
<div class="abs news-item" style="top:950px"><h3>March 17</h3>10:00am-1:00pm- at Borough Kitchen: 1580 Fifth Avenue at 104th Street, New York, NY</div>
<div class="abs view-all">view all &gt;&gt;</div>

<div class="abs tile-photo plum" style="left:376px;top:832px;width:296px;background:radial-gradient(ellipse 20% 14% at 50% 42%,#6a4a32 0,rgba(106,74,50,0) 100%),linear-gradient(90deg,#c46fc8 20%,#f2e8d6 20%,#efe2c8 80%,#c46fc8 80%)" role="img" aria-label="Handmade baklava product label"></div>
<div class="abs tile-label plum" style="left:374px;top:1020px;width:298px"><span>Nadia's Dune Pantry Products</span><span>&gt;&gt;</span></div>
<div class="abs tile-photo" style="left:685px;top:832px;width:297px;background:radial-gradient(ellipse 25% 18% at 55% 35%,#e88a20 0,rgba(232,138,32,0) 100%),radial-gradient(ellipse 32% 14% at 55% 55%,#7aa4c0 0,rgba(122,164,192,0) 100%),linear-gradient(#4a3e38,#8a7a70 45%,#b8aaa0 70%,#8a7868)" role="img" aria-label="Blue ceramic bowl of orange cherry tomatoes on a wooden table"></div>
<div class="abs tile-label" style="left:685px;top:1020px;width:297px"><span>Suggestion and Question Box</span><span>&gt;&gt;</span></div>

<footer class="abs site-footer"></footer>
<div class="abs footer-nav">Home<span>|</span>Why Mediterranean &amp; MidEast Cuisine?<span>|</span>Cooking Class<span>|</span>Healthy Recipes<span>|</span>About<span>|</span>Contact</div>
<div class="abs copyright">Copyright © 2012 Sumac up</div>
<div class="abs social-large" style="left:752px">Share</div>
<div class="abs social-large" style="left:805px">Follow</div>
<div class="abs social-large" style="left:858px">Mail</div>
</body>
</html>
```